Web-site design for company trading in chemicals & lubricants

We need a standard 5 page web-site designed for our company based in Dubai, UAE.
The web-site should highlight our capacity to store material as well as distribute the same. The products we sell are basic chemicals - packed in bags as well as drums. Bags are big bags - 25 kgs each as well as drums - 200 litres each. We want to highlight the fact that we huge stocks of this material & can deliver by sea & road,
Please use this site as a ref - http://www.norvex-solvents.co.uk/
Besides this, we need a page dedicated to finished products that we are selling for use in the auto industry - lubricants, motor oils,brake-fluids, greases, coolants etc. This are packed in large drums as well as small cans.
It would be nice if the site could immediately also provide a ref. to our location - Dubai or that we are based in the Middle East.
We will provide our company logo for reference

```html
<!DOCTYPE html>
<html lang="en">
<head>
<meta charset="utf-8">
<title>Dunecrest – Chemicals &amp; Lubricants Trading, Dubai</title>
<link rel="stylesheet" href="https://fonts.googleapis.com/css2?family=Open+Sans:wght@400;700&family=PT+Sans:wght@400;700&display=swap">
<style>
:root{
  --orange:#d9472a;
  --orange-dark:#c23a20;
  --brown:#5a2e1c;
  --brown-dark:#432012;
  --gold:#a28b2c;
  --gold-dark:#8a7422;
  --olive-head:#7a6420;
  --text:#333;
  --line:#bdbdbd;
  --panel:#ececec;
  --white:#fff;
}
*{box-sizing:border-box;margin:0;padding:0}
html,body{width:903px;height:1200px;overflow:hidden;background:var(--white)}
body{position:relative;font-family:"PT Sans",Arial,sans-serif;color:var(--text)}
.abs{position:absolute}

/* header */
.brand{left:76px;top:52px;display:flex;align-items:center;gap:10px}
.brand-name{font-family:"Open Sans",Arial,sans-serif;font-weight:700;font-size:27px;letter-spacing:3px;color:var(--brown)}
.brand-dot{width:22px;height:22px;border-radius:50%;background:var(--gold)}
.search{left:574px;top:33px;width:190px;height:23px;border:1px solid #aaa;border-radius:4px;font-size:13px;color:#666;padding:3px 9px}
.search-btn{left:777px;top:34px;width:52px;height:20px;background:var(--gold);border-radius:3px}
.search-btn svg{display:block;margin:2px auto}
.main-nav{left:292px;top:71px;width:536px;height:37px;background:var(--orange);border-radius:7px;display:flex;align-items:center;padding-left:2px}
.main-nav a{color:var(--white);text-decoration:none;font-size:17px;white-space:nowrap;text-align:center;height:37px;line-height:41px;border-right:1px solid rgba(0,0,0,.15)}
.main-nav a:last-child{border-right:0}
.sub-nav{right:74px;top:121px;font-size:14px;color:#333;white-space:nowrap}

/* hero */
.hero{left:76px;top:147px;width:752px;height:289px;border:1px solid #ccc;border-radius:12px}
.hero-title{left:80px;top:7px;width:311px;text-align:right;font-family:"Open Sans",Arial,sans-serif;font-weight:700;font-size:24px;line-height:31px;letter-spacing:-.2px;color:#1a1a1a}
.hero-text{left:6px;top:104px;width:400px;font-size:13.5px;line-height:16px;letter-spacing:-.15px}
.read-more{right:366px;top:154px;font-size:14px;color:var(--orange)}
.hero-rule{left:6px;top:178px;width:385px;border-top:1px solid #999}
.arrow{font-size:34px;color:#999;font-family:"Open Sans",Arial,sans-serif;line-height:1}
.thumb{top:198px;width:96px;height:73px}
.thumb-1{left:41px;background:linear-gradient(135deg,#c7a060,#e7e0d6 50%,#8a5a3a)}
.thumb-2{left:150px;background:linear-gradient(135deg,#9bc3e0,#3d6fa8 60%,#b26a3a)}
.thumb-3{left:266px;width:100px;height:76px;top:196px;border:1px solid #999;background:linear-gradient(180deg,#fff,#d7d7d7 55%,#c23a20 85%,#e9e9e9)}
.hero-photo{left:407px;top:14px;width:325px;height:244px;background:linear-gradient(180deg,#e3a44a 0%,#b66a24 40%,#5b3414 70%,#2a170a 100%)}
.hero-caption{right:20px;top:267px;font-size:10px;color:#333}

/* category buttons */
.cat{top:450px;height:49px;border-radius:6px;color:var(--white);font-family:"Open Sans",Arial,sans-serif;font-weight:700;font-size:18.5px;white-space:nowrap;display:flex;align-items:center;overflow:hidden}
.cat .chev{font-size:24px;opacity:.45;margin-left:14px;flex:none}
.cat-industrial{left:76px;width:232px;background:linear-gradient(180deg,#b09a3a,var(--gold-dark))}
.cat-industrial .chev{width:41px}
.cat-pharma{left:336px;width:232px;background:linear-gradient(180deg,#6a3a26,var(--brown-dark))}
.cat-pharma .chev{width:29px;color:#c0502a;opacity:.8}
.cat-personal{left:595px;width:233px;background:linear-gradient(180deg,#e35a3a,var(--orange-dark))}
.cat-personal .chev{width:46px;color:#8e2612;opacity:.5}

/* section headings */
.section-title{font-family:"Open Sans",Arial,sans-serif;font-weight:700;font-size:20px;line-height:24px;padding-bottom:2px}
.rule{border-top:1px solid}

/* partners */
.partners{left:76px;top:557px;width:492px;height:121px;background:var(--panel);border:1px solid #d2d2d2;border-radius:10px}
.badge{top:36px;height:46px;background:#c9c9c9;border-radius:6px}

/* news */
.news{left:76px;top:688px;width:490px;height:470px;border-radius:10px;background:linear-gradient(180deg,#f4f4f4 0,#fff 70px)}
.news-title{left:11px;top:6px;color:var(--orange)}
.news-item-title{font-weight:700;font-size:14px;color:#333;white-space:nowrap}
.news-img{width:118px;height:80px}
.news-text{font-size:13.5px;line-height:15px;color:#333}
.more{right:17px;top:447px;font-size:14px;color:var(--orange)}

/* product selector */
.selector{left:595px;top:570px;width:233px;height:209px;background:var(--panel);border-radius:10px}
.sel-label{left:18px;font-size:14px;color:#444}
.sel{left:18px;width:199px;height:20px;background:var(--white);border:1px solid #aaa;border-radius:3px}
.sel::before{content:"";position:absolute;left:9px;right:30px;top:9px;border-top:1px solid #333}
.sel-btn{position:absolute;right:0;top:0;width:20px;height:18px;background:linear-gradient(180deg,#eee,#bbb);border-left:1px solid #999;border-radius:0 3px 3px 0}
.sel-btn svg{display:block;margin:6px auto}
.sel-search{left:142px;top:182px;width:72px;height:19px;background:var(--orange);color:var(--white);font-weight:700;font-size:13px;text-align:center;line-height:19px;border-radius:3px}

/* contact */
.map{left:598px;top:832px;width:215px;height:132px;background:linear-gradient(160deg,#dcc0a3,#cfae8c);border-radius:30px 60px 20px 50px}
.contact-info{left:595px;top:970px;font-size:14px;line-height:15.5px;color:#555;font-style:normal}
.social{top:1088px;width:58px;height:58px;border-radius:8px;background:linear-gradient(180deg,#a9a9a9,#6e6e6e);border:2px solid #ddd}

/* footer */
.footer{left:76px;top:1172px;width:752px;height:28px;background:var(--orange);border-radius:7px 7px 0 0;color:var(--white);font-size:14px;line-height:30px;white-space:nowrap}
.footer-links{position:absolute;left:18px}
.footer-copy{position:absolute;right:26px}
</style>
</head>
<body>

<header>
  <div class="abs brand"><span class="brand-name">DUNECREST</span><span class="brand-dot"></span></div>
  <div class="abs search">Search...</div>
  <div class="abs search-btn"><svg width="16" height="16" viewBox="0 0 16 16"><circle cx="6.5" cy="6.5" r="4.5" fill="none" stroke="#fff" stroke-width="2.2"/><line x1="10" y1="10" x2="14.5" y2="14.5" stroke="#fff" stroke-width="2.6" stroke-linecap="round"/></svg></div>
  <nav class="abs main-nav">
    <a href="#" style="width:63px">HOME</a><a href="#" style="width:99px">ABOUT US</a><a href="#" style="width:100px">PARTNERS</a><a href="#" style="width:95px">LOGISTIC</a><a href="#" style="width:64px">NEWS</a><a href="#" style="width:111px">CONTACT US</a>
  </nav>
  <div class="abs sub-nav">INDUSTRIAL | PHARMACEUTICAL | PERSONAL CARE | PRODUCT SELECTOR</div>
</header>

<section class="abs hero">
  <h1 class="abs hero-title">We huge stocks of this material &amp; can deliver by sea &amp; road</h1>
  <p class="abs hero-text">There are many variations of passages of Lorem Ipsum available, but the majority have suffered alteration in some form, by injected humour or randomised words which don't look even slightly believable.</p>
  <a class="abs read-more">Read more »</a>
  <div class="abs hero-rule"></div>
  <span class="abs arrow" style="left:7px;top:210px">‹</span>
  <div class="abs thumb thumb-1" role="img" aria-label="Laboratory worker handling chemical samples"></div>
  <div class="abs thumb thumb-2" role="img" aria-label="Test tubes with coloured liquids"></div>
  <div class="abs thumb thumb-3" role="img" aria-label="Lubricant cans in grey and red"></div>
  <span class="abs arrow" style="left:376px;top:210px">›</span>
  <div class="abs hero-photo" role="img" aria-label="Container ship at a port with cranes at sunset"></div>
  <div class="abs hero-caption">We huge stocks of this material &amp; can deliver</div>
</section>

<a class="abs cat cat-industrial"><span class="chev">»</span><span>INDUSTRIAL</span></a>
<a class="abs cat cat-pharma"><span class="chev">»</span><span>PHARMACEUTICAL</span></a>
<a class="abs cat cat-personal"><span class="chev">»</span><span>PERSONAL CARE</span></a>

<h2 class="abs section-title" style="left:76px;top:522px;color:var(--brown)">PARTNERS</h2>
<div class="abs rule" style="left:76px;top:546px;width:492px;border-color:var(--brown)"></div>
<section class="abs partners">
  <span class="abs arrow" style="left:14px;top:41px">‹</span>
  <div class="abs badge" style="left:48px;width:98px"></div>
  <div class="abs badge" style="left:170px;width:118px"></div>
  <div class="abs badge" style="left:314px;width:142px"></div>
  <span class="abs arrow" style="left:467px;top:41px">›</span>
</section>

<section class="abs news">
  <h2 class="abs section-title news-title">LATEST NEWS</h2>
  <div class="abs rule" style="left:11px;top:32px;width:462px;border-color:var(--orange)"></div>

  <h3 class="abs news-item-title" style="left:13px;top:43px">Contrary to popular belief, Lorem Ipsum is not simply random text.</h3>
  <div class="abs news-img" style="left:14px;top:69px;background:linear-gradient(135deg,#8d97a3,#d9dde2 45%,#2f3a4a)" role="img" aria-label="Engineer in hard hat beside industrial equipment"></div>
  <p class="abs news-text" style="left:149px;top:70px;width:330px">Contrary to popular belief, Lorem Ipsum is not simply random text. It has roots in a piece of classical Latin literature from 45 BC, making it over 2000 years old. Harold Whitcombe, a Latin professor at Marlowe College in Virginia, looked up.</p>
  <div class="abs rule" style="left:13px;top:164px;width:460px;border-color:var(--line)"></div>

  <h3 class="abs news-item-title" style="left:12px;top:176px">There are many variations of passages of Lorem Ipsum available</h3>
  <div class="abs news-img" style="left:13px;top:206px;background:linear-gradient(135deg,#3a5a1a,#e0c040 40%,#b02a20 70%,#2a5aa0)" role="img" aria-label="Bottles of coloured chemicals with pellets"></div>
  <p class="abs news-text" style="left:137px;top:206px;width:340px">There are many variations of passages of Lorem Ipsum available, but the majority have suffered alteration in some form, by injected humour, or randomised words which don't look even slightly believable. If you are going to use a passage of Lorem Ipsum</p>
  <div class="abs rule" style="left:13px;top:299px;width:460px;border-color:var(--line)"></div>

  <h3 class="abs news-item-title" style="left:17px;top:306px">Contrary to popular belief, Lorem Ipsum is not simply random text.</h3>
  <div class="abs news-img" style="left:13px;top:332px;height:99px;background:linear-gradient(180deg,#d98a3a,#8a3a14 55%,#2a1206)" role="img" aria-label="Industrial storage tanks at dusk"></div>
  <p class="abs news-text" style="left:145px;top:343px;width:335px">Contrary to popular belief, Lorem Ipsum is not simply random text. It has roots in a piece of classical Latin literature from 45 BC, making it over 2000 years old. Harold Whitcombe, a Latin professor at Marlowe College in Virginia, looked up.</p>
  <div class="abs rule" style="left:13px;top:442px;width:460px;border-color:var(--line)"></div>
  <a class="abs more">More News »</a>
</section>

<h2 class="abs section-title" style="left:595px;top:522px;color:var(--brown)">PRODUCT SELECTOR</h2>
<div class="abs rule" style="left:595px;top:546px;width:233px;border-color:var(--brown)"></div>
<form class="abs selector">
  <span class="abs sel-label" style="top:5px">Division:</span>
  <div class="abs sel" style="top:24px"><span class="sel-btn"><svg width="10" height="6" viewBox="0 0 10 6"><path d="M1 1l4 4 4-4" fill="none" stroke="#444" stroke-width="1.6"/></svg></span></div>
  <span class="abs sel-label" style="top:48px">Market:</span>
  <div class="abs sel" style="top:66px"><span class="sel-btn"><svg width="10" height="6" viewBox="0 0 10 6"><path d="M1 1l4 4 4-4" fill="none" stroke="#444" stroke-width="1.6"/></svg></span></div>
  <span class="abs sel-label" style="top:89px">Functionality:</span>
  <div class="abs sel" style="top:107px"><span class="sel-btn"><svg width="10" height="6" viewBox="0 0 10 6"><path d="M1 1l4 4 4-4" fill="none" stroke="#444" stroke-width="1.6"/></svg></span></div>
  <span class="abs sel-label" style="top:132px">Product:</span>
  <div class="abs sel" style="top:148px"><span class="sel-btn"><svg width="10" height="6" viewBox="0 0 10 6"><path d="M1 1l4 4 4-4" fill="none" stroke="#444" stroke-width="1.6"/></svg></span></div>
  <span class="abs sel-search">Search »</span>
</form>

<h2 class="abs section-title" style="left:596px;top:799px;color:var(--olive-head)">CONTACT US</h2>
<div class="abs rule" style="left:596px;top:822px;width:232px;border-color:var(--olive-head)"></div>
<div class="abs map" role="img" aria-label="Map of Asia and the Middle East marking Dubai, India, Russia and Australia"></div>
<address class="abs contact-info">Dunecrest ©<br>Tel. 3210004567<br>Email. info@dunecrest.com<br>Address: Dubai</address>

<h2 class="abs section-title" style="left:597px;top:1051px;color:var(--orange)">FOLLOW US</h2>
<div class="abs rule" style="left:597px;top:1074px;width:231px;border-color:var(--orange)"></div>
<a class="abs social" style="left:597px" aria-label="Social network"></a>
<a class="abs social" style="left:665px" aria-label="Social network"></a>
<a class="abs social" style="left:739px" aria-label="Social network"></a>

<footer class="abs footer">
  <span class="footer-links">Home | About Us | Partners | Logistic | News | Contact Us</span>
  <span class="footer-copy">Dunecrest ©&nbsp; 2011</span>
</footer>

</body>
</html>
```